IT services company requires Letterhead design

We need a professional letterhead designed to be used for general correspondence with customers, quotes, invoices etc. We are a new IT services company specialising in computer servicing and repairs and mobile and tablet repairs. Attached are templates that my printing company have supplied, my logos, an interpretation of our website for you to get a feel of the company. Details to be included on the letterhead are

Company Number – 4738261
VAT Number - 518337942
Registered Address – 14-16 Brambly Lane, London, E4 9QT

Phone – 01632 487215
Email – sales@quorvent.com
Web – www.quorvent.com

I would prefer for the top of the letterhead to just have the company logo on a white background and the rest of the details on the bottom of the letterhead but I am open to design ideas.

Thanks

```html
<!DOCTYPE html>
<html lang="en">
<head>
<meta charset="utf-8">
<title>Quorvent Letterhead</title>
<link href="https://fonts.googleapis.com/css2?family=Jost:wght@400;600&family=Arimo:wght@400;700&display=swap" rel="stylesheet">
<style>
  :root {
    --backdrop: #e6e6e6;
    --paper: #fdfdfd;
    --ink: #3a3a3c;
    --ink-soft: #555557;
    --brand-blue: #2fc0e3;
    --brand-dark: #3b3b3d;
  }
  * { box-sizing: border-box; margin: 0; padding: 0; }
  html, body { width: 1200px; height: 1200px; overflow: hidden; }
  body { background: var(--backdrop); position: relative; font-family: "Arimo", Arial, sans-serif; color: var(--ink); }

  .letterhead {
    position: absolute; left: 211px; top: 50px;
    width: 778px; height: 1100px;
    background: var(--paper);
    box-shadow: 0 2px 10px rgba(0,0,0,0.12);
    overflow: hidden;
  }
  .corner-mark { position: absolute; left: 62px; top: 0; width: 44px; height: 26px; }

  .brand-name {
    position: absolute; left: 78px; top: 74px;
    font-family: "Jost", sans-serif; font-weight: 600; font-size: 44px;
    color: var(--brand-dark); letter-spacing: 0.5px;
  }

  .contact-list {
    position: absolute; right: 66px; top: 52px;
    list-style: none;
    font-family: "Jost", sans-serif; font-size: 13px; color: var(--ink);
  }
  .contact-list li { display: flex; align-items: center; justify-content: flex-end; gap: 7px; line-height: 19px; }
  .contact-list svg { width: 11px; height: 11px; fill: var(--brand-blue); flex: none; }
  .contact-address {
    position: absolute; right: 66px; top: 140px;
    display: flex; align-items: center; gap: 7px;
    font-family: "Jost", sans-serif; font-size: 13px; color: var(--ink);
  }
  .contact-address svg { width: 11px; height: 11px; fill: var(--brand-blue); flex: none; }

  .letter-body {
    position: absolute; left: 96px; top: 270px; width: 585px;
    font-size: 10.5px; line-height: 14px; color: var(--ink-soft);
  }
  .letter-body .salutation { margin-bottom: 24px; }
  .letter-body p { margin-bottom: 18px; text-align: justify; }

  .sign-off { position: absolute; left: 96px; top: 725px; font-size: 10.5px; color: var(--ink); }
  .sign-off .signer { font-weight: 700; }
  .sign-off .signature {
    display: block; width: 110px; height: 36px; margin: 6px 0 4px 8px;
    background: linear-gradient(90deg, rgba(47,192,227,0.25), rgba(47,192,227,0.08));
    border-radius: 4px;
  }

  .registration {
    position: absolute; left: 96px; top: 962px;
    font-family: "Jost", sans-serif; font-size: 13px; line-height: 20px; color: var(--ink);
  }
  .registration .label { color: var(--brand-blue); }

  .footer-swoosh { position: absolute; left: 0; bottom: 0; width: 778px; height: 300px; }
</style>
</head>
<body>
  <main class="letterhead">
    <svg class="corner-mark" viewBox="0 0 44 26" aria-hidden="true"><polygon points="0,0 44,0 32,26" fill="var(--brand-blue)"/></svg>

    <div class="brand-name">Quorvent</div>

    <ul class="contact-list">
      <li>www.quorvent.com <svg viewBox="0 0 12 12"><circle cx="6" cy="6" r="5.5"/></svg></li>
      <li>01632 487215 <svg viewBox="0 0 12 12"><path d="M2 1l2.5 0 1 3-1.5 1c.7 1.5 1.5 2.3 3 3l1-1.5 3 1V10c0 .8-.7 1.2-1.5 1C5 10.5 1.5 7 1 2.5 .9 1.7 1.3 1 2 1z"/></svg></li>
      <li>sales@quorvent.com <svg viewBox="0 0 12 12"><path d="M0 2h12v8H0z M0 2l6 4.5L12 2" stroke="#fff" stroke-width="0.8"/></svg></li>
    </ul>
    <div class="contact-address">
      14-16 Brambly Lane, London, E4 9QT
      <svg viewBox="0 0 12 12"><path d="M6 0a4 4 0 0 0-4 4c0 3 4 8 4 8s4-5 4-8a4 4 0 0 0-4-4zm0 5.5a1.5 1.5 0 1 1 0-3 1.5 1.5 0 0 1 0 3z"/></svg>
    </div>

    <section class="letter-body">
      <p class="salutation">Dear Sir,</p>
      <p>Lorem Ipsum is simply dummy text of the printing and typesetting industry. Lorem Ipsum has been the industry's standard dummy text ever since the 1500s, when an unknown printer took a galley of type and scrambled it to make a type specimen book. It has survived not only five centuries, but also the leap into electronic typesetting, remaining essentially unchanged. It was popularised in the 1960s with the release of Typeloom sheets containing Lorem Ipsum passages, and more recently with desktop publishing software like Pressline Studio including versions of Lorem Ipsum.</p>
      <p>Lorem Ipsum is simply dummy text of the printing and typesetting industry. Lorem Ipsum has been the industry's standard dummy text ever since the 1500s, when an unknown printer took a galley of type and scrambled it to make a type specimen book. It has survived not only five centuries, but also the leap into electronic typesetting.</p>
      <p>Lorem Ipsum is simply dummy text of the printing and typesetting industry. Lorem Ipsum has been the industry's standard dummy text ever since the 1500s, when an unknown printer took a galley of type and scrambled it to make a type.</p>
      <p>Lorem Ipsum is simply dummy text of the printing and typesetting industry. Lorem Ipsum has been the industry's standard dummy text ever since the 1500s, when an unknown printer took a galley of type and scrambled it to make a type specimen book. It has survived not only five centuries, but also the leap into electronic typesetting, remaining essentially unchanged. It was popularised in the 1960s with the release of Typeloom sheets containing Lorem Ipsum passages, and more recently with desktop publishing software like Pressline Studio including versions of Lorem Ipsum. Lorem Ipsum is simply dummy text of the printing and typesetting industry. Lorem Ipsum has been the industry's standard dummy text ever since the 1500s, when an unknown printer took a galley of type and scrambled it to make a type specimen book. It has survived not only five centuries, but also the leap into electronic typesetting.</p>
      <p>Lorem Ipsum is simply dummy text of the printing and typesetting industry. Lorem Ipsum has been the industry's standard dummy text ever since the 1500s, when an unknown printer took a galley of type and scrambled it to make a type.</p>
    </section>

    <div class="sign-off">
      <div class="signer">Daniel Hart</div>
      <span class="signature" role="img" aria-label="Handwritten signature of Daniel Hart"></span>
      <div class="role">Director</div>
    </div>

    <div class="registration">
      <div><span class="label">Company Number</span> – 4738261</div>
      <div><span class="label">VAT Number</span> - 518337942</div>
    </div>

    <svg class="footer-swoosh" viewBox="0 0 778 300" preserveAspectRatio="none" aria-hidden="true">
      <path d="M330 292 C520 262 660 232 778 182 L778 212 C650 248 500 275 330 292 Z" fill="var(--brand-dark)"/>
      <path d="M0 300 C300 286 560 260 778 222 L778 300 Z" fill="var(--brand-blue)"/>
    </svg>
  </main>
</body>
</html>
```